Figma App design and working prototype

I need to create a User Interface design and a Working prototype using Figma or similar. I’d also like all the assets and guidelines needed to guide the App developers to create the final product.
So, I'll need Design files and assets but you that I can give to an App development company or a freelance developer to create Android and iOS apps.

This app is an app for adults who wan to meet and have sex no strings attached.

The App name will be Nuvora

I have attached an app some pictures and a pdf file explaining details of the apps functions.

This app will be a sexy version of the pobalo app with a personals section used for adult services. I have attached images and a pdf below that will tell you the functions of the app.

I need an app interface design done for an app idea I have. I am nee to this it is my first time trying to launch an app and I do not know what you need in order to get what I need. I need a site map/ design and if possible a working prototype that I can pass on to an app developer that can deliver the final product. This model will be used to raise funds and give investors an idea of what the apps functions will do as detailed in the project brief. Any advise would be greatly appreciated. Please let me know if you have any questions. Looking forward to working with you.

Target Market(s)

Adults men and women looking for some adult entertainment

Industry/Entity Type

Adult entertainment Strip clubs

Colors
E54698
E96AAD
F1A4CE
F9D9EA
FCEFF6
A7469A
B969AE
D3A5CF
EDDBEB
F8F0F9
6B429C
8869AF
B7A5CE
E3DAEB
F3F0F8

Requirements
Must have
• An 18+ confirmation,
Nice to have
• A sexy feel.

```html
<!DOCTYPE html>
<html lang="en">
<head>
<meta charset="utf-8">
<title>Nuvora – App Screens</title>
<link href="https://fonts.googleapis.com/css2?family=Poppins:wght@400;500;600;700&display=swap" rel="stylesheet">
<style>
:root{
  --bg:#b99292;
  --dark:#333333;
  --pink:#e91e79;
  --pink-soft:#e96aad;
  --text:#333333;
  --muted:#777777;
  --line:#e2e2e2;
  --panel-grey:#f3f3f3;
  --white:#ffffff;
  --map-a:#cfe6c8;
  --map-b:#a9d49d;
}
*{box-sizing:border-box;margin:0;padding:0}
html,body{width:831px;height:1200px;overflow:hidden;background:var(--bg);font-family:'Poppins',sans-serif;color:var(--text)}
.stage{position:absolute;left:0;top:0;width:1592px;height:2300px;transform:scale(0.52198);transform-origin:0 0}
.screen{position:absolute;top:45px;width:450px;background:var(--white);overflow:hidden}
.screen--profile{left:48px;height:1674px}
.screen--services{left:556px;height:2170px}
.screen--location{left:1063px;height:1229px}

.app-header{background:var(--dark);height:163px;position:relative;color:var(--white)}
.brand{position:absolute;left:12px;top:24px;font-size:26px;font-weight:600;letter-spacing:.3px}
.header-actions{position:absolute;right:13px;top:24px;display:flex;align-items:center;gap:14px;font-size:14px;font-weight:600}
.lang{display:flex;align-items:center;gap:6px}
.btn-post{background:var(--pink);color:var(--white);height:42px;padding:0 14px;display:flex;align-items:center;font-weight:600;font-size:15px}
.search{position:absolute;left:13px;right:13px;top:93px;height:54px;background:var(--white);color:var(--text);display:flex;align-items:center;justify-content:space-between;padding:0 16px;font-size:16px}

.gallery{display:grid;grid-template-columns:repeat(3,134px);gap:11px 11px;padding:14px 13px 0 13px}
.gallery .photo{height:104px}
.details{padding:14px 13px 0 14px}
.row{height:48px;border-bottom:1px solid var(--line);display:flex;align-items:center;font-size:15px}
.row .label{width:144px;flex:none}
.row .value{color:var(--pink)}
.row .select{display:flex;align-items:center;gap:10px}
.row .wide{width:162px}
.checks{display:flex;gap:8px;color:var(--pink)}
.checks span{display:flex;align-items:center;gap:5px}
.box{width:12px;height:12px;border:1.5px solid var(--text);display:inline-block}

.contact{margin:18px 13px 0 13px;background:var(--panel-grey);padding:22px 19px 28px;font-size:15px}
.contact p{display:flex;align-items:center;height:37px;white-space:nowrap}
.contact .k{margin-right:12px}
.contact .v{color:var(--pink)}
.phone{margin-left:26px;display:flex;align-items:center;gap:8px;color:var(--pink)}
.messengers{margin-left:22px;display:flex;gap:8px}
.messengers span{display:flex;align-items:center;gap:3px;font-size:12px;color:var(--pink)}
.messengers i{width:14px;height:14px;border-radius:50%;background:var(--pink-soft);display:inline-block}
.actions{display:flex;gap:10px;margin-top:18px;margin-left:2px}
.btn{height:49px;display:flex;align-items:center;justify-content:center;font-weight:600;font-size:15px}
.btn-dark{background:var(--dark);color:var(--white);width:209px}
.btn-outline{border:1.5px solid var(--dark);width:141px}

.tabbar{position:absolute;left:0;right:0;bottom:0;height:64px;background:#f6f6f6;border-top:1px solid var(--line);display:flex;justify-content:space-around;align-items:center;font-size:14px;color:var(--muted)}
.tab{display:flex;flex-direction:column;align-items:center;gap:1px}
.tab--active{color:var(--pink)}

.section-title{height:57px;background:var(--panel-grey);display:flex;align-items:center;padding-left:13px;color:var(--pink);font-size:21px;font-weight:600}
.service-list{list-style:none;padding:0 13px}
.service-list li{height:48px;border-bottom:1px solid var(--line);display:flex;align-items:center;font-size:15px}
.service-list .box{margin-right:24px}
.service-list .count{color:var(--pink-soft);margin-left:16px}

.picker-bar{height:57px;display:flex;align-items:center;justify-content:space-between;padding:0 15px;font-size:17px;font-weight:500}
.picker-bar .done{color:var(--pink)}
.map{position:relative;height:730px;background:radial-gradient(circle at 50% 45%,#e9b7ce 0,#d7d9c4 32%,var(--map-a) 55%,var(--map-b) 100%)}
.refine{position:absolute;left:0;right:0;top:0;height:128px;background:rgba(60,60,60,.75);color:var(--white);padding:12px 12px 0}
.refine strong{font-weight:700;font-size:16px}
.refine span{font-size:15px;margin-left:6px}
.loc-search{margin-top:13px;height:53px;background:var(--white);color:var(--text);display:flex;align-items:center;justify-content:space-between;padding:0 16px;font-size:16px}
.distance{padding:28px 13px 0}
.distance .head{display:flex;justify-content:space-between;font-size:18px;font-weight:600}
.distance .head b{color:var(--pink);font-weight:500}
.slider{position:relative;height:8px;background:#eee;border-radius:4px;margin-top:28px}
.slider .fill{position:absolute;left:0;top:0;height:8px;width:178px;background:var(--pink);border-radius:4px}
.slider .knob{position:absolute;left:166px;top:-8px;width:24px;height:24px;border-radius:50%;background:var(--pink);border:3px solid var(--white);box-shadow:0 0 0 1px #ddd}
.btn-apply{margin-top:30px;height:58px;background:var(--dark);color:var(--white);display:flex;align-items:center;justify-content:center;font-size:19px;font-weight:600}
</style>
</head>
<body>
<div class="stage">

<section class="screen screen--profile">
  <header class="app-header">
    <div class="brand">Nuvora</div>
    <div class="header-actions">
      <span class="lang">EN <svg width="10" height="7" viewBox="0 0 10 7"><path d="M1 1l4 4 4-4" stroke="#fff" stroke-width="2" fill="none"/></svg></span>
      <span>SIGN IN</span>
      <span class="btn-post">POST AD</span>
    </div>
    <div class="search">Search keyword
      <svg width="20" height="24" viewBox="0 0 20 24"><path d="M10 1a8 8 0 0 0-8 8c0 6 8 14 8 14s8-8 8-14a8 8 0 0 0-8-8z" fill="none" stroke="#333" stroke-width="1.5"/><circle cx="10" cy="9" r="3" fill="none" stroke="#333" stroke-width="1.5"/></svg>
    </div>
  </header>

  <div class="gallery">
    <div class="photo" role="img" aria-label="Profile photo 1" style="background:linear-gradient(135deg,#3e4552,#b9ae9c)"></div>
    <div class="photo" role="img" aria-label="Profile photo 2" style="background:linear-gradient(135deg,#2a1a22,#6b4553)"></div>
    <div class="photo" role="img" aria-label="Profile photo 3" style="background:linear-gradient(135deg,#4a4442,#8c7769)"></div>
    <div class="photo" role="img" aria-label="Profile photo 4" style="background:linear-gradient(135deg,#1b2328,#7a5546)"></div>
    <div class="photo" role="img" aria-label="Profile photo 5" style="background:linear-gradient(135deg,#e9e2da,#a57e66)"></div>
    <div class="photo" role="img" aria-label="Profile photo 6" style="background:linear-gradient(135deg,#eef0f1,#b78d77)"></div>
  </div>

  <div class="details">
    <div class="row"><span class="label">Gender:</span><span class="value">Female</span></div>
    <div class="row"><span class="label">Age:</span><span class="value">26</span></div>
    <div class="row"><span class="label">Location:</span><span class="value">Brazil</span></div>
    <div class="row"><span class="label">Eye colour:</span><span class="value">Brazil</span></div>
    <div class="row"><span class="label">Hair colour:</span><span class="select">Select <svg width="8" height="12" viewBox="0 0 8 12"><path d="M4 0l4 5H0zM4 12l4-5H0z" fill="#333"/></svg></span></div>
    <div class="row"><span class="label">Hair length:</span><span class="value">Blond</span></div>
    <div class="row"><span class="label">Bust size:</span><span class="select">Select <svg width="8" height="12" viewBox="0 0 8 12"><path d="M4 0l4 5H0zM4 12l4-5H0z" fill="#333"/></svg></span></div>
    <div class="row"><span class="label">Bust type:</span><span class="select">Select <svg width="8" height="12" viewBox="0 0 8 12"><path d="M4 0l4 5H0zM4 12l4-5H0z" fill="#333"/></svg></span></div>
    <div class="row"><span class="label">Travel:</span><span class="select">Select <svg width="8" height="12" viewBox="0 0 8 12"><path d="M4 0l4 5H0zM4 12l4-5H0z" fill="#333"/></svg></span></div>
    <div class="row"><span class="label">Weight:</span><span class="value">58kg</span></div>
    <div class="row"><span class="label">Height:</span><span class="select">Select <svg width="8" height="12" viewBox="0 0 8 12"><path d="M4 0l4 5H0zM4 12l4-5H0z" fill="#333"/></svg></span></div>
    <div class="row"><span class="label">Ethnicity:</span><span class="select">Select <svg width="8" height="12" viewBox="0 0 8 12"><path d="M4 0l4 5H0zM4 12l4-5H0z" fill="#333"/></svg></span></div>
    <div class="row"><span class="label wide">Sexual Orientation:</span><span class="value">Strait, Gay, Lesbian, Bisexual</span></div>
    <div class="row"><span class="label">Smoker:</span><span class="select">Select <svg width="8" height="12" viewBox="0 0 8 12"><path d="M4 0l4 5H0zM4 12l4-5H0z" fill="#333"/></svg></span></div>
    <div class="row"><span class="label">Nationality:</span><span class="value">58kg</span></div>
    <div class="row"><span class="label">Languages:</span><span class="value">58kg</span></div>
    <div class="row"><span class="label">Available for:</span><span class="checks"><span><i class="box"></i>Outcall</span><span><i class="box"></i>Incall</span><span><i class="box"></i>Virtual</span></span></div>
    <div class="row"><span class="label">Meeting with:</span><span class="checks"><span><i class="box"></i>Men</span><span><i class="box"></i>Women</span></span></div>
    <div class="row" style="border-bottom:none"><span class="label">Services:</span><span class="value">Anal</span></div>
  </div>

  <div class="contact">
    <p><span class="k">Fans Link:</span><span class="v">Dolor sit amet</span>
      <span class="phone"><svg width="14" height="14" viewBox="0 0 14 14"><path d="M3 1l2 3-1 1.5c.8 1.8 2 3 3.5 3.5L9 8l3 2-1 2.5C6 12 2 8 1.5 3z" fill="#333"/></svg>1-800-55012</span></p>
    <p><span class="k">Website:</span><span class="v">www.nuvsite.com</span>
      <span class="messengers"><span><i></i>Chatly</span><span><i></i>Wirely</span><span><i></i>Sigline</span></span></p>
    <p><span class="k">Email:</span><span class="v">info@nuvmail.com</span></p>
    <div class="actions"><span class="btn btn-dark">Make An Appointment</span><span class="btn btn-outline">Pay Now</span></div>
  </div>

  <nav class="tabbar">
    <span class="tab tab--active"><svg width="16" height="14" viewBox="0 0 16 14"><path d="M8 0l8 7h-2v7H10V9H6v5H2V7H0z" fill="currentColor"/></svg>Home</span>
    <span class="tab"><svg width="14" height="14" viewBox="0 0 14 14"><circle cx="7" cy="4" r="3.5" fill="#666"/><path d="M0 14c0-4 3-6 7-6s7 2 7 6z" fill="#666"/></svg>My Lounge</span>
    <span class="tab"><svg width="14" height="12" viewBox="0 0 14 12"><path d="M0 3h4l1-2h4l1 2h4v9H0z" fill="#666"/><circle cx="7" cy="7" r="2.5" fill="#f6f6f6"/></svg>Post AD</span>
    <span class="tab"><svg width="15" height="13" viewBox="0 0 15 13"><path d="M7.5 13L1 6.5A3.7 3.7 0 0 1 7.5 1.5 3.7 3.7 0 0 1 14 6.5z" fill="#666"/></svg>Favourites</span>
    <span class="tab"><svg width="15" height="11" viewBox="0 0 15 11"><rect width="15" height="11" fill="#666"/><path d="M0 0l7.5 6L15 0" stroke="#f6f6f6" fill="none"/></svg>Messages</span>
  </nav>
</section>

<section class="screen screen--services">
  <header class="app-header">
    <div class="brand">Nuvora</div>
    <div class="header-actions">
      <span class="lang">EN <svg width="10" height="7" viewBox="0 0 10 7"><path d="M1 1l4 4 4-4" stroke="#fff" stroke-width="2" fill="none"/></svg></span>
      <span>SIGN IN</span>
      <span class="btn-post">POST AD</span>
    </div>
    <div class="search">Search keyword
      <svg width="20" height="24" viewBox="0 0 20 24"><path d="M10 1a8 8 0 0 0-8 8c0 6 8 14 8 14s8-8 8-14a8 8 0 0 0-8-8z" fill="none" stroke="#333" stroke-width="1.5"/><circle cx="10" cy="9" r="3" fill="none" stroke="#333" stroke-width="1.5"/></svg>
    </div>
  </header>
  <h2 class="section-title">Services Provided</h2>
  <ul class="service-list">
    <li><i class="box"></i>69<span class="count">(254812)</span></li>
    <li><i class="box"></i>Anal<span class="count">(254812)</span></li>
    <li><i class="box"></i>Bondage<span class="count">(254812)</span></li>
    <li><i class="box"></i>Casual photos<span class="count">(254812)</span></li>
    <li><i class="box"></i>Classic sex<span class="count">(254812)</span></li>
    <li><i class="box"></i>Couples<span class="count">(254812)</span></li>
    <li><i class="box"></i>Cum in face<span class="count">(254812)</span></li>
    <li><i class="box"></i>Cum in mouth<span class="count">(254812)</span></li>
    <li><i class="box"></i>Cum on body<span class="count">(254812)</span></li>
    <li><i class="box"></i>Cunnilingus - Fingering<span class="count">(254812)</span></li>
    <li><i class="box"></i>Deep throat<span class="count">(254812)</span></li>
    <li><i class="box"></i>Dirty talk<span class="count">(254812)</span></li>
    <li><i class="box"></i>Domination<span class="count">(254812)</span></li>
    <li><i class="box"></i>Duo with girl<span class="count">(254812)</span></li>
    <li><i class="box"></i>Erotic message<span class="count">(254812)</span></li>
    <li><i class="box"></i>Foot fetish<span class="count">(254812)</span></li>
    <li><i class="box"></i>French kissing<span class="count">(254812)</span></li>
    <li><i class="box"></i>GFE<span class="count">(254812)</span></li>
    <li><i class="box"></i>Golden Shower giving<span class="count">(254812)</span></li>
    <li><i class="box"></i>Golden shower received<span class="count">(254812)</span></li>
    <li><i class="box"></i>Group sex<span class="count">(254812)</span></li>
    <li><i class="box"></i>Handjobs<span class="count">(254812)</span></li>
    <li><i class="box"></i>Kamasutra<span class="count">(254812)</span></li>
    <li><i class="box"></i>Masturbation<span class="count">(254812)</span></li>
    <li><i class="box"></i>Mistress<span class="count">(254812)</span></li>
    <li><i class="box"></i>Oral without condom<span class="count">(254812)</span></li>
    <li><i class="box"></i>Porn star experience<span class="count">(254812)</span></li>
    <li><i class="box"></i>Rimming giving<span class="count">(254812)</span></li>
    <li><i class="box"></i>Rimming receiving<span class="count">(254812)</span></li>
    <li><i class="box"></i>Role-play<span class="count">(254812)</span></li>
    <li><i class="box"></i>Sex between breasts<span class="count">(254812)</span></li>
    <li><i class="box"></i>Sex toys<span class="count">(254812)</span></li>
    <li><i class="box"></i>Squirting<span class="count">(254812)</span></li>
    <li><i class="box"></i>Striptease<span class="count">(254812)</span></li>
    <li><i class="box"></i>Submissive<span class="count">(254812)</span></li>
    <li><i class="box"></i>Swallowing<span class="count">(254812)</span></li>
    <li><i class="box"></i>Uniform<span class="count">(254812)</span></li>
    <li><i class="box"></i>Video with sex<span class="count">(254812)</span></li>
    <li style="border-bottom:none"><i class="box"></i>With 2 men<span class="count">(254812)</span></li>
  </ul>
  <nav class="tabbar">
    <span class="tab tab--active"><svg width="16" height="14" viewBox="0 0 16 14"><path d="M8 0l8 7h-2v7H10V9H6v5H2V7H0z" fill="currentColor"/></svg>Home</span>
    <span class="tab"><svg width="14" height="14" viewBox="0 0 14 14"><circle cx="7" cy="4" r="3.5" fill="#666"/><path d="M0 14c0-4 3-6 7-6s7 2 7 6z" fill="#666"/></svg>My Lounge</span>
    <span class="tab"><svg width="14" height="12" viewBox="0 0 14 12"><path d="M0 3h4l1-2h4l1 2h4v9H0z" fill="#666"/><circle cx="7" cy="7" r="2.5" fill="#f6f6f6"/></svg>Post AD</span>
    <span class="tab"><svg width="15" height="13" viewBox="0 0 15 13"><path d="M7.5 13L1 6.5A3.7 3.7 0 0 1 7.5 1.5 3.7 3.7 0 0 1 14 6.5z" fill="#666"/></svg>Favourites</span>
    <span class="tab"><svg width="15" height="11" viewBox="0 0 15 11"><rect width="15" height="11" fill="#666"/><path d="M0 0l7.5 6L15 0" stroke="#f6f6f6" fill="none"/></svg>Messages</span>
  </nav>
</section>

<section class="screen screen--location">
  <header class="app-header">
    <div class="brand">Nuvora</div>
    <div class="header-actions">
      <span class="lang">EN <svg width="10" height="7" viewBox="0 0 10 7"><path d="M1 1l4 4 4-4" stroke="#fff" stroke-width="2" fill="none"/></svg></span>
      <span>SIGN IN</span>
      <span class="btn-post">POST AD</span>
    </div>
    <div class="search">Search keyword
      <svg width="20" height="24" viewBox="0 0 20 24"><path d="M10 1a8 8 0 0 0-8 8c0 6 8 14 8 14s8-8 8-14a8 8 0 0 0-8-8z" fill="none" stroke="#333" stroke-width="1.5"/><circle cx="10" cy="9" r="3" fill="none" stroke="#333" stroke-width="1.5"/></svg>
    </div>
  </header>
  <div class="picker-bar"><span>Cancel</span><span>Choose Location</span><span class="done">Done</span></div>
  <div class="map" role="img" aria-label="Street map of the selected area with a search radius">
    <svg width="450" height="730" style="position:absolute;left:0;top:0">
      <circle cx="225" cy="382" r="179" fill="rgba(233,30,121,.12)" stroke="#e91e79" stroke-width="1.5"/>
      <circle cx="226" cy="375" r="9" fill="#fff" stroke="#e91e79" stroke-width="2"/>
    </svg>
    <div class="refine">
      <strong>Refine</strong><span>(484,5874 results)</span>
      <div class="loc-search">Search Location
        <svg width="20" height="20" viewBox="0 0 20 20"><circle cx="8" cy="8" r="6" fill="none" stroke="#333" stroke-width="2.2"/><path d="M12.5 12.5L18 18" stroke="#333" stroke-width="2.4"/></svg>
      </div>
    </div>
  </div>
  <div class="distance">
    <div class="head"><span>Distance</span><b>100km</b></div>
    <div class="slider"><span class="fill"></span><span class="knob"></span></div>
    <div class="btn-apply">Apply</div>
  </div>
  <nav class="tabbar">
    <span class="tab tab--active"><svg width="16" height="14" viewBox="0 0 16 14"><path d="M8 0l8 7h-2v7H10V9H6v5H2V7H0z" fill="currentColor"/></svg>Home</span>
    <span class="tab"><svg width="14" height="14" viewBox="0 0 14 14"><circle cx="7" cy="4" r="3.5" fill="#666"/><path d="M0 14c0-4 3-6 7-6s7 2 7 6z" fill="#666"/></svg>My Lounge</span>
    <span class="tab"><svg width="14" height="12" viewBox="0 0 14 12"><path d="M0 3h4l1-2h4l1 2h4v9H0z" fill="#666"/><circle cx="7" cy="7" r="2.5" fill="#f6f6f6"/></svg>Post AD</span>
    <span class="tab"><svg width="15" height="13" viewBox="0 0 15 13"><path d="M7.5 13L1 6.5A3.7 3.7 0 0 1 7.5 1.5 3.7 3.7 0 0 1 14 6.5z" fill="#666"/></svg>Favourites</span>
    <span class="tab"><svg width="15" height="11" viewBox="0 0 15 11"><rect width="15" height="11" fill="#666"/><path d="M0 0l7.5 6L15 0" stroke="#f6f6f6" fill="none"/></svg>Messages</span>
  </nav>
</section>

</div>
</body>
</html>
```